Label

I need a label designed for a bottle of water. I like the lightning bolt and the blue. But I do not want it exactly like the Zimm-ooh.

The label needs to be 9 inches by 2.5 inches.

Logo Text

Mesa Spring: Sip the Mesa

```html
<!DOCTYPE html>
<html lang="en">
<head>
<meta charset="utf-8">
<title>Mesa Spring: Sip the Mesa – Bottle Label</title>
<link href="https://fonts.googleapis.com/css2?family=Comfortaa:wght@700&family=Exo+2:wght@500&family=Kanit:wght@500&display=swap" rel="stylesheet">
<style>
  :root {
    --page-bg: #ffffff;
    --label-top: #0a4d8c;
    --label-bottom: #0884b9;
    --ink-light: #ffffff;
    --ink-brand: #0a5b98;
    --pattern-tint: rgba(255, 255, 255, 0.07);
  }
  * { margin: 0; padding: 0; box-sizing: border-box; }
  html, body {
    width: 820px;
    height: 1200px;
    overflow: hidden;
    background: var(--page-bg);
  }
  .canvas {
    position: relative;
    width: 820px;
    height: 1200px;
    display: flex;
    align-items: center;
    justify-content: center;
  }
  /* 9 in × 2.5 in wrap label = 3.6 : 1 */
  .label {
    position: relative;
    width: 792px;
    height: 220px;
    background: linear-gradient(180deg, var(--label-top) 0%, var(--label-bottom) 100%);
    color: var(--ink-light);
    text-align: center;
    overflow: hidden;
  }
  .drop-pattern {
    position: absolute;
    inset: 0;
    background:
      radial-gradient(ellipse 60px 80px at 12% 40%, var(--pattern-tint), transparent 70%),
      radial-gradient(ellipse 50px 70px at 88% 30%, var(--pattern-tint), transparent 70%),
      radial-gradient(ellipse 45px 60px at 30% 85%, var(--pattern-tint), transparent 70%),
      radial-gradient(ellipse 55px 70px at 72% 80%, var(--pattern-tint), transparent 70%);
  }
  .brand-mark {
    position: absolute;
    left: 50%;
    top: 18px;
    width: 56px;
    height: 56px;
    margin-left: -28px;
    border: 2.5px solid var(--ink-light);
    border-radius: 50%;
  }
  .brand-name {
    position: absolute;
    left: 0;
    right: 0;
    top: 84px;
    font-family: "Comfortaa", sans-serif;
    font-weight: 700;
    font-size: 40px;
    line-height: 1;
    letter-spacing: -0.5px;
    color: var(--ink-light);
  }
  .tagline {
    position: absolute;
    left: 50%;
    top: 134px;
    transform: translateX(-50%);
    padding: 1px 9px 2px;
    background: var(--ink-light);
    color: var(--ink-brand);
    font-family: "Exo 2", sans-serif;
    font-weight: 500;
    font-size: 18px;
    line-height: 1.05;
    letter-spacing: 1.2px;
    white-space: nowrap;
  }
  .volume {
    position: absolute;
    left: 0;
    right: 0;
    top: 182px;
    font-family: "Kanit", sans-serif;
    font-weight: 500;
    font-size: 11px;
    line-height: 1;
    color: var(--ink-light);
  }
</style>
</head>
<body>
  <main class="canvas">
    <section class="label" aria-label="Mesa Spring bottle label">
      <div class="drop-pattern" role="img" aria-label="Faint scattered raindrop pattern across the label background"></div>
      <div class="brand-mark" aria-hidden="true"></div>
      <h1 class="brand-name">Mesa Spring</h1>
      <p class="tagline">Sip the Mesa</p>
      <p class="volume">1 Liter(33.8 fl. oz)</p>
    </section>
  </main>
</body>
</html>
```